Builder Website Brackwell Construction

Hi,
Brackwell Construction is a domestic builder on the Gold Coast specializing in new homes, townhouses, duplexes and high end renovations.
Brackwell Construction can make your dream new home or development a reality. Whether you already have plans or require a complete design and construct project service, Brackwell Construction will make your project a stress free experience.
We offer design, town planning, certification and construction services.

Target Market(s)

Anyone looking to build.

Industry/Entity Type

Building

Coding

Coded - Design and coding required

Font styles to use
Other font styles liked:
• Match logo

Colors

Designer to choose colors to be used in the design.

Requirements
Must have
• Attractive home page with logo etc.
• About us page
• Gallery page
• Services Page
• Contact us page

```html
<!DOCTYPE html>
<html lang="en">
<head>
<meta charset="utf-8">
<title>Brackwell Construction</title>
<link href="https://fonts.googleapis.com/css2?family=Montserrat:wght@300;400;500;600&family=Lato:wght@400;700&display=swap" rel="stylesheet">
<style>
:root{
  --navy:#17133a;
  --navy-deep:#120f2e;
  --ink:#1d1d24;
  --muted:#5a5a62;
  --soft:#b8b8bd;
  --grey-band:#ececec;
  --white:#ffffff;
  --line:#d9d9dc;
}
*{margin:0;padding:0;box-sizing:border-box}
html,body{width:1200px;height:3061px;overflow:hidden}
body{position:relative;background:var(--white);font-family:"Lato",Arial,sans-serif;color:var(--ink)}
.abs{position:absolute}
.heading{font-family:"Montserrat",Arial,sans-serif;font-weight:500;font-size:40px;color:var(--ink);text-align:center;width:1200px;left:0;letter-spacing:.5px}

/* header */
.site-header{top:0;left:0;width:1200px;height:102px;background:var(--white)}
.emergency{top:0;right:0;width:378px;height:35px;background:var(--navy);color:var(--white);font-family:"Montserrat",sans-serif;font-size:13px;line-height:35px;padding-left:36px;clip-path:polygon(0 0,100% 0,100% 100%,22px 100%)}
.brand-box{top:0;left:61px;width:164px;height:157px;background:var(--white);z-index:3;clip-path:polygon(0 0,100% 0,100% 100%,50% 90%,0 100%);box-shadow:0 2px 6px rgba(0,0,0,.2);display:flex;flex-direction:column;align-items:center;padding-top:14px}
.brand-ring{width:66px;height:66px;border:2px solid var(--navy);border-radius:50%}
.brand-name{font-family:"Montserrat",sans-serif;font-weight:400;font-size:26px;color:var(--navy);margin-top:6px}
.main-nav{top:62px;left:598px;display:flex;gap:0}
.main-nav a,.foot-nav a{font-family:"Montserrat",sans-serif;font-size:15px;color:var(--ink);text-decoration:none;letter-spacing:.3px}
.main-nav a{margin-right:42px}

/* hero */
.hero{top:102px;left:0;width:1200px;height:516px;background:linear-gradient(180deg,#3a3f46 0%,#2b3036 45%,#4b4a46 78%,#1f2226 100%)}
.hero-title{top:300px;width:1200px;text-align:center;font-family:"Montserrat",sans-serif;font-size:37px;color:var(--white);font-weight:300;letter-spacing:1.5px}
.hero-title b{font-weight:600}
.play{top:384px;left:578px;width:44px;height:44px;border-radius:50%;background:#111;border:2px solid #888}
.hero-arrows{top:572px;left:580px}

/* welcome */
.welcome-title{top:676px}
.welcome-title .light{font-weight:300;color:#6a6a70}
.welcome-title b{font-weight:600}
.welcome-copy{top:742px;left:150px;width:900px;text-align:center;font-size:14.5px;line-height:24px;color:var(--muted)}
.btn-dark{top:837px;left:527px;width:146px;height:41px;background:var(--navy);color:var(--white);border-radius:6px;font-family:"Montserrat",sans-serif;font-size:14px;text-align:center;line-height:41px}

/* gallery */
.gallery-band{top:930px;left:0;width:1200px;height:654px;background:var(--grey-band)}
.gallery-title{top:954px}
.tile{position:absolute}
.g-arrow{top:1202px}

/* services */
.services-title{top:1627px}
.service{top:1704px;width:262px;height:264px;text-align:center;padding-top:26px}
.service.active{background:var(--navy);color:var(--white)}
.service h3{font-family:"Montserrat",sans-serif;font-weight:500;font-size:29px;margin-top:10px}
.service p{font-size:12px;line-height:21px;width:210px;margin:10px auto 0;color:inherit}
.service .sep{position:absolute;right:0;top:24px;height:200px;width:1px;background:var(--line)}
.btn-outline-sm{display:inline-block;margin-top:14px;width:108px;height:28px;border:1px solid var(--white);border-radius:6px;font-family:"Montserrat",sans-serif;font-size:11px;line-height:26px}

/* testimonials */
.testi-band{top:2023px;left:0;width:1200px;height:414px;background:var(--grey-band)}
.testi-title{top:2054px}
.testi{top:2123px;width:326px;height:259px;background:#f9f9f9;box-shadow:0 1px 6px rgba(0,0,0,.18);text-align:center;padding-top:28px}
.testi p{font-size:14.5px;line-height:28px;color:var(--muted);width:270px;margin:14px auto 0}
.testi .who{font-size:14.5px;color:var(--soft);margin-top:14px}

/* contact */
.contact{top:2437px;left:0;width:1200px;height:443px;background:var(--navy-deep)}
.contact-title{top:2464px;color:var(--white)}
.info{left:102px;color:var(--white);font-size:16.5px;line-height:25px;display:flex;gap:18px}
.field{position:absolute;background:var(--white);font-family:"Montserrat",sans-serif;font-size:12px;color:#333;padding:8px 22px}
.submit{top:2753px;left:510px;width:108px;height:39px;border:1px solid #bbb;border-radius:8px;color:var(--white);font-family:"Montserrat",sans-serif;font-size:13px;text-align:center;line-height:37px}

/* footer */
.foot-brand{top:2896px;left:74px;display:flex;flex-direction:column;align-items:center}
.foot-brand .brand-ring{width:70px;height:70px}
.foot-brand .brand-name{font-size:27px}
.foot-nav{top:2912px;left:592px}
.foot-nav a{margin-right:40px}
.social{top:2956px;left:1022px;display:flex;gap:22px}
.social span{width:14px;height:14px;border-radius:50%;background:var(--ink);display:block}
.copyright{top:3003px;left:856px;font-size:15px;color:#444}
</style>
</head>
<body>

<header class="site-header abs">
  <div class="emergency abs">24/7 Emergency Number 1.800.555.0142</div>
  <nav class="main-nav abs">
    <a href="#">HOME</a><a href="#">ABOUT US</a><a href="#">GALLERY</a><a href="#">SERVICES</a><a href="#">CONTACT US</a>
  </nav>
</header>
<div class="brand-box abs"><div class="brand-ring"></div><div class="brand-name">brackwell</div></div>

<section class="hero abs" role="img" aria-label="City skyline of high-rise towers at sunset over an empty road"></section>
<h1 class="hero-title abs">brackwell <b>constructions.</b></h1>
<svg class="play abs" viewBox="0 0 44 44" aria-hidden="true"><polygon points="18,14 18,30 30,22" fill="#fff"/></svg>
<svg class="hero-arrows abs" width="40" height="20" viewBox="0 0 40 20"><path d="M10 4 L5 10 L10 16" stroke="#fff" stroke-width="2.5" fill="none"/><path d="M30 4 L35 10 L30 16" stroke="#fff" stroke-width="2.5" fill="none"/></svg>

<section>
  <h2 class="heading welcome-title abs">welcome to <span class="light">brackwell</span> <b>constructions</b></h2>
  <p class="welcome-copy abs">Nulla nisi nulla, condimentum ac ante sed, tempor interdum tortor. Integer porttitor nisl in neque tempus, ut blandit sem efficitur. Vivamus consequat leo eget lorem facilisis suscipit. Maecenas vestibulum nisi ut dolor faucibus molestie. Aliquam sodales ultricies iaculis. Proin nunc nisl, maximus in libero at, pretium mollis metus. Aenean diam massa, condimentum.</p>
  <div class="btn-dark abs">READ MORE</div>
</section>

<section class="gallery-band abs"></section>
<h2 class="heading gallery-title abs">gallery</h2>
<div class="tile" style="left:73px;top:1025px;width:256px;height:222px;background:linear-gradient(160deg,#9fb4c9,#b9b2a2 60%,#5d6b52)" role="img" aria-label="Multi-storey heritage style apartment building"></div>
<div class="tile" style="left:343px;top:1025px;width:251px;height:273px;background:linear-gradient(180deg,#2a2a66,#1f1d4a)" role="img" aria-label="Modern apartment tower facade"></div>
<svg class="abs" style="left:448px;top:1141px" width="40" height="40" viewBox="0 0 40 40"><circle cx="20" cy="20" r="19" fill="#111" stroke="#fff" stroke-width="1.5"/><path d="M20 13v14M13 20h14" stroke="#fff" stroke-width="2"/></svg>
<div class="tile" style="left:606px;top:1025px;width:253px;height:200px;background:linear-gradient(180deg,#6f86a8,#c9a98a 70%,#5a4a3e)" role="img" aria-label="Rooftop pergola terrace beside a tower at dusk"></div>
<div class="tile" style="left:873px;top:1025px;width:254px;height:200px;background:linear-gradient(140deg,#e9e7e4,#b9a58c 60%,#8a7a68)" role="img" aria-label="Cutaway 3D floor plan of a home interior"></div>
<div class="tile" style="left:73px;top:1265px;width:256px;height:262px;background:linear-gradient(180deg,#6d86b5,#d8d5d0 50%,#6e6a60)" role="img" aria-label="White modern house entrance with pathway"></div>
<div class="tile" style="left:343px;top:1314px;width:251px;height:213px;background:linear-gradient(180deg,#6a9ad8,#b3b8c0 45%,#8a5a44 70%,#4f7a3a)" role="img" aria-label="Brick townhouses on a suburban street"></div>
<div class="tile" style="left:606px;top:1237px;width:521px;height:290px;background:linear-gradient(170deg,#202a3a,#5b5247 55%,#c48a4a 80%,#3b2e24)" role="img" aria-label="Contemporary concrete house lit at night"></div>
<svg class="g-arrow abs" style="left:44px" width="14" height="20"><path d="M10 4 L4 10 L10 16" stroke="#111" stroke-width="2.5" fill="none"/></svg>
<svg class="g-arrow abs" style="left:1144px" width="14" height="20"><path d="M4 4 L10 10 L4 16" stroke="#111" stroke-width="2.5" fill="none"/></svg>

<section>
  <h2 class="heading services-title abs">services</h2>
  <div class="service abs" style="left:73px">
    <svg width="60" height="60" viewBox="0 0 60 60" fill="none" stroke="#555" stroke-width="2"><rect x="6" y="6" width="48" height="48"/><path d="M6 22h20V6M26 38h28M36 22v16M14 32h6v14h-6z"/></svg>
    <h3>design</h3><p>Nemo enim ipsam vptatem quia vtas sit aspernatur aut odit aut f</p><span class="sep"></span>
  </div>
  <div class="service active abs" style="left:339px">
    <svg width="60" height="60" viewBox="0 0 60 60" fill="none" stroke="#fff" stroke-width="2"><path d="M6 30 L30 8 L54 30M12 26v26h36V26M20 36h8v8h-8zM34 36h8v8h-8zM24 18l12 12"/></svg>
    <h3>town planning</h3><p>Nemo enim ipsam vptatem quia vtas sit aspernatur aut odit aut f</p><span class="btn-outline-sm">READ MORE</span>
  </div>
  <div class="service abs" style="left:606px">
    <svg width="60" height="60" viewBox="0 0 60 60" fill="none" stroke="#555" stroke-width="2"><rect x="12" y="6" width="36" height="46" rx="3"/><path d="M18 16h24M18 24h24M18 32h14"/><circle cx="40" cy="44" r="6"/></svg>
    <h3>certification</h3><p>Nemo enim ipsam vptatem quia vtas sit aspernatur aut odit aut f</p><span class="sep"></span>
  </div>
  <div class="service abs" style="left:873px">
    <svg width="60" height="60" viewBox="0 0 60 60" fill="none" stroke="#555" stroke-width="2"><path d="M10 34a20 20 0 0 1 40 0zM6 34h48v5H6zM26 14h8v20h-8z"/><path d="M18 39c2 10 22 10 24 0"/></svg>
    <h3>construction</h3><p>Nemo enim ipsam vptatem quia vtas sit aspernatur aut odit aut f</p>
  </div>
</section>

<section class="testi-band abs"></section>
<h2 class="heading testi-title abs">testimonials</h2>
<div class="testi abs" style="left:75px">
  <svg width="44" height="36" viewBox="0 0 44 36" fill="#777"><path d="M2 34V20C2 10 8 4 16 2l2 4c-5 2-8 6-8 10h8v18zM24 34V20c0-10 6-16 14-18l2 4c-5 2-8 6-8 10h8v18z"/></svg>
  <p>Nemo enim ipsam vptatem quia vtas sit aspernatur aut odit aut fugit, sed quia conse-quuntur magni dolores eos qui ratione vo-luptatem sequi</p><div class="who">- Maren T.</div>
</div>
<div class="testi abs" style="left:437px">
  <svg width="44" height="36" viewBox="0 0 44 36" fill="#777"><path d="M2 34V20C2 10 8 4 16 2l2 4c-5 2-8 6-8 10h8v18zM24 34V20c0-10 6-16 14-18l2 4c-5 2-8 6-8 10h8v18z"/></svg>
  <p>Nemo enim ipsam vptatem quia vtas sit aspernatur aut odit aut fugit, sed quia conse-quuntur magni dolores eos qui ratione vo-luptatem sequi</p><div class="who">- Maren T.</div>
</div>
<div class="testi abs" style="left:800px">
  <svg width="44" height="36" viewBox="0 0 44 36" fill="#777"><path d="M2 34V20C2 10 8 4 16 2l2 4c-5 2-8 6-8 10h8v18zM24 34V20c0-10 6-16 14-18l2 4c-5 2-8 6-8 10h8v18z"/></svg>
  <p>Nemo enim ipsam vptatem quia vtas sit aspernatur aut odit aut fugit, sed quia conse-quuntur magni dolores eos qui ratione vo-luptatem sequi</p><div class="who">- Maren T.</div>
</div>

<section class="contact abs"></section>
<h2 class="heading contact-title abs" style="font-weight:400">contact us</h2>
<div class="info abs" style="top:2555px">
  <svg width="14" height="20" viewBox="0 0 14 20" style="margin-top:4px"><path d="M7 0a7 7 0 0 0-7 7c0 5 7 13 7 13s7-8 7-13a7 7 0 0 0-7-7z" fill="#fff"/><circle cx="7" cy="7" r="2.5" fill="#120f2e"/></svg>
  <div>Harbourline Business Centre<br>18 Keel Street<br>Southport,<br>QLD 4215</div>
</div>
<div class="info abs" style="top:2673px">
  <svg width="16" height="18" viewBox="0 0 16 18" style="margin-top:4px"><path d="M3 1l3 4-2 2c1 3 3 5 6 6l2-2 4 3-2 3C7 17 0 9 1 3z" fill="#fff"/></svg>
  <div>1-800 555 0177</div>
</div>
<div class="info abs" style="top:2715px">
  <svg width="18" height="14" viewBox="0 0 18 14" style="margin-top:6px"><rect width="18" height="14" rx="1" fill="#fff"/><path d="M1 1l8 7 8-7" stroke="#120f2e" stroke-width="1.5" fill="none"/></svg>
  <div>hello@brackwellbuild.com</div>
</div>
<div class="field" style="left:508px;top:2547px;width:302px;height:37px">NAME</div>
<div class="field" style="left:822px;top:2547px;width:305px;height:37px">EMAIL</div>
<div class="field" style="left:508px;top:2598px;width:619px;height:35px">PHONE</div>
<div class="field" style="left:508px;top:2649px;width:619px;height:86px">MESSAGE</div>
<div class="submit abs">SUBMIT</div>

<footer>
  <div class="foot-brand abs"><div class="brand-ring"></div><div class="brand-name">brackwell</div></div>
  <nav class="foot-nav abs"><a href="#">HOME</a><a href="#">ABOUT US</a><a href="#">GALLERY</a><a href="#">SERVICES</a><a href="#">CONTACT US</a></nav>
  <div class="social abs" aria-label="Social links"><span></span><span></span><span></span></div>
  <div class="copyright abs">© 2018 &nbsp;|&nbsp; www.brackwellbuild.com</div>
</footer>

</body>
</html>
```